Electronic call to action mailer

I am launching my new web site and would like to send an electronic mailer to a segmented base. The base would be mostly mothers with children and I want them to shop at my new web site.

I would like to include a call to action - if they register as members they will get 20% off their first purchase and a 10% thereafter as members.

They will also be in a lucky draw contest for a $500 voucher to use at our wen site.
Updates

I have updated the details I require. As this is a call to action page, it should be really catchy that we brand new company that promises to bring quality children's products to them. The company's vision is pinned to producing and distributing organic products and products that are produced with fair trade practices.

Reason: I was late in updating my brief and I think there are a few designs that I already like. I just need to have the updates in

Target Market(s)

Parents that are interested in quality products for kids

Industry/Entity Type

Electronic

Font styles to use
Sans Serif

Colors
c1b2d3
86cfc6
f04a50

Requirements
Must have
• I page that is really easy to get the message. 5 consolation prizes that will be from the Tiny Amber Sprouts toiletry range. (picture included). Winner gets $500 worth of goods (at RRP)
Must mention that this is in conjunction with the launch of our new on-line shop.
Must mention that our range of clothes are new to Singapore and we have exclusivity with the brands
terms and conditions apply
Nice to have
• A catchy tag line, making them want to become a member

```html
<!DOCTYPE html>
<html lang="en">
<head>
<meta charset="utf-8">
<title>Register Now – Member Offer Mailer</title>
<link rel="stylesheet" href="https://fonts.googleapis.com/css2?family=Mulish:wght@700;800&family=Questrial&display=swap">
<style>
  :root {
    --page-bg: #e6e6e6;
    --sheet-bg: #ffffff;
    --sky-blue: #29a8e0;
    --deep-blue: #0071bc;
    --leaf-green: #8dc63f;
    --lilac: #c1b2d3;
    --teal: #86cfc6;
    --coral: #f04a50;
    --ink: #555555;
    --icon-grey: #7f7f7f;
    --white: #ffffff;
  }
  * { margin: 0; padding: 0; box-sizing: border-box; }
  html, body {
    width: 1200px; height: 807px; overflow: hidden;
    background: var(--page-bg);
  }
  .sheet {
    position: absolute; left: 131px; top: 0;
    width: 938px; height: 807px;
    background: var(--sheet-bg);
  }
  .launch-note {
    position: absolute; left: 24px; top: 22px;
    width: 889px; height: 40px;
    display: flex; align-items: center; justify-content: center; gap: 12px;
    font-family: "Questrial", sans-serif; font-size: 18px;
    color: var(--ink);
    border-top: 4px solid var(--teal);
    border-bottom: 4px solid var(--lilac);
  }
  .launch-note strong {
    font-family: "Mulish", sans-serif; font-weight: 800;
    color: var(--coral);
  }
  .hero {
    position: absolute; left: 24px; top: 79px;
    width: 889px; height: 281px;
  }
  .hero-photo {
    position: absolute; inset: 0;
    background:
      radial-gradient(ellipse at 40% 35%, #e9b48f 0%, rgba(233,180,143,0) 28%),
      linear-gradient(180deg, #9cc870 0%, #7fb04e 45%, #c9e3b0 75%, #8fbd5c 100%);
  }
  .hero-banner {
    position: absolute; left: 0; top: 156px;
    width: 693px; height: 109px;
    background: var(--sky-blue);
    color: var(--white);
    padding: 6px 0 0 16px;
  }
  .hero-title {
    font-family: "Mulish", sans-serif; font-weight: 800;
    font-size: 50px; line-height: 56px; letter-spacing: 0.5px;
  }
  .hero-sub {
    font-family: "Questrial", sans-serif;
    font-size: 27px; line-height: 32px;
  }
  .cta-bar {
    position: absolute; left: 24px; top: 387px;
    width: 889px; height: 62px;
    background: var(--leaf-green);
    color: var(--white);
    display: flex; align-items: center; justify-content: space-between;
    padding: 0 22px 0 16px;
    font-family: "Mulish", sans-serif; font-weight: 800;
    font-size: 30px; letter-spacing: 0.4px; text-decoration: none;
  }
  .cta-arrow { width: 26px; height: 36px; }
  .feature {
    position: absolute; top: 477px;
    width: 267px; height: 141px;
    color: var(--white);
    padding: 18px 16px 0 16px;
  }
  .feature--quality { left: 24px; background: var(--sky-blue); }
  .feature--shipping { left: 331px; background: var(--deep-blue); }
  .feature-title {
    font-family: "Mulish", sans-serif; font-weight: 800;
    font-size: 29px; line-height: 36px; margin-bottom: 8px;
  }
  .feature-text {
    font-family: "Questrial", sans-serif;
    font-size: 22px; line-height: 28px;
  }
  .shop-tile {
    position: absolute; left: 635px; top: 477px;
    width: 267px; height: 141px;
    background:
      radial-gradient(ellipse at 65% 45%, #f0cdb4 0%, rgba(240,205,180,0) 45%),
      linear-gradient(135deg, #f4f8fb 0%, #d7e6f0 45%, #a9c8dc 100%);
  }
  .shop-label {
    position: absolute; left: 12px; top: 6px;
    font-family: "Mulish", sans-serif; font-weight: 800;
    font-size: 22px; color: var(--sky-blue);
  }
  .lucky-draw {
    position: absolute; left: 24px; top: 630px;
    width: 889px; height: 28px;
    display: flex; align-items: center;
    padding-left: 12px;
    border-left: 6px solid var(--coral);
    font-family: "Questrial", sans-serif; font-size: 16px;
    color: var(--ink); white-space: nowrap;
  }
  .lucky-draw strong {
    font-family: "Mulish", sans-serif; font-weight: 800;
    color: var(--coral); margin-right: 6px;
  }
  .divider {
    position: absolute; left: 24px; top: 669px;
    width: 880px; height: 2px;
  }
  .footer-note {
    position: absolute; left: 24px; top: 700px;
    width: 600px;
    font-family: "Questrial", sans-serif; font-size: 15px; line-height: 22px;
    color: var(--ink);
  }
  .footer-note .tagline {
    font-family: "Mulish", sans-serif; font-weight: 800;
    font-size: 18px; color: var(--deep-blue);
  }
  .footer-note .terms { font-size: 13px; color: var(--icon-grey); }
  .social {
    position: absolute; top: 703px; width: 70px;
    display: flex; flex-direction: column; align-items: center; gap: 4px;
    font-family: "Questrial", sans-serif; font-size: 13px;
    color: var(--icon-grey); text-decoration: none;
  }
  .social-dot {
    width: 47px; height: 47px; border-radius: 50%;
    background: var(--icon-grey);
  }
  .social--friendly { left: 668px; }
  .social--chirper { left: 756px; }
  .social--circlenet { left: 844px; }
</style>
</head>
<body>
  <main class="sheet">
    <p class="launch-note"><strong>Our new online shop is open!</strong> Clothing brands new to Singapore – and exclusive to us.</p>

    <section class="hero">
      <div class="hero-photo" role="img" aria-label="Photo of a smiling mother and daughter lying in a flowering spring meadow"></div>
      <div class="hero-banner">
        <h1 class="hero-title">REGISTER NOW</h1>
        <p class="hero-sub">members they will get 20% off their first purchase</p>
      </div>
    </section>

    <a class="cta-bar" href="#register">
      <span>REGISTER NOW and get 10% member dicount here</span>
      <svg class="cta-arrow" viewBox="0 0 26 36" aria-hidden="true">
        <polyline points="5,3 20,18 5,33" fill="none" stroke="#ffffff" stroke-width="6"/>
      </svg>
    </a>

    <div class="feature feature--quality">
      <h2 class="feature-title">Qality Items</h2>
      <p class="feature-text">Designer brands<br>resonable prices</p>
    </div>
    <div class="feature feature--shipping">
      <h2 class="feature-title">Free Shipping</h2>
      <p class="feature-text">Next day shipping<br>for free</p>
    </div>
    <div class="shop-tile" role="img" aria-label="Photo of a smiling mother hugging her young daughter by the sea">
      <span class="shop-label">Shop now</span>
    </div>

    <p class="lucky-draw"><strong>Lucky draw:</strong> members can win $500 of goods (at RRP) + 5 consolation prizes from the Tiny Amber Sprouts toiletry range</p>

    <svg class="divider" viewBox="0 0 880 2" aria-hidden="true">
      <line x1="0" y1="1" x2="880" y2="1" stroke="#8a8a8a" stroke-width="1.5" stroke-dasharray="12 10"/>
    </svg>

    <div class="footer-note">
      <p class="tagline">Join the family – organic, fair-trade goodness for little ones.</p>
      <p class="terms">*Terms and conditions apply.</p>
    </div>

    <a class="social social--friendly" href="#"><span class="social-dot"></span>Friendly</a>
    <a class="social social--chirper" href="#"><span class="social-dot"></span>Chirper</a>
    <a class="social social--circlenet" href="#"><span class="social-dot"></span>Circlenet</a>
  </main>
</body>
</html>
```